Divi Theme Wordpress Web Design

Hi,

We have had a Divi theme website running on Wordpress for a few years but need a fresh refresh.

Designs must be possible with standard Divi theme and minimal/no CSS customisation or similar. if this is required please note this in submission. Also, please note mobile and device usage which must be universal.

We have our logo files attached, plus some research and sample sites we have done, plus all of our current collateral. We will need a few examples such as landing (main) page, single blog post and software specific page. See current examples below:

Landing (Main) - http://www.pelrandata.example/inventory-wholesale-manufacturing/

Single Blog Post - http://www.pelrandata.example/why-remote-work-made-break-most-relaxing-ever/

Software Page - http://www.pelrandata.example/software-implementation/tolvek-stock-implementation-and-training/

Target Market(s)

small businesses, small business owners, people who need simple but technical computer help,

Industry/Entity Type

Professional Service

Number of Pages Required

3 page

Requirements
Must have
• see attachment guide
Nice to have
• see attachment guide

```html
<!DOCTYPE html>
<html lang="en">
<head>
<meta charset="utf-8">
<title>Pelran Data – Inventory Solutions</title>
<link href="https://fonts.googleapis.com/css2?family=Nunito+Sans:wght@300;400;600;700&family=Open+Sans:wght@400;600&display=swap" rel="stylesheet">
<style>
:root{
  --teal:#00b3b9;
  --teal-dark:#00a2a8;
  --teal-icon:#1cb8bf;
  --text:#444b52;
  --muted:#9aa0a6;
  --grey-band:#f2f2f2;
  --red:#b3202f;
  --orange:#f07f3c;
  --blue:#1f5f86;
  --step-teal:#2aa4ad;
  --navy-btn:#1d6585;
  --white:#ffffff;
}
*{margin:0;padding:0;box-sizing:border-box}
html,body{width:1200px;height:3536px;overflow:hidden}
body{position:relative;font-family:"Nunito Sans",sans-serif;color:var(--text);background:var(--white)}
.abs{position:absolute}

/* Hero */
.hero{position:absolute;left:0;top:0;width:1200px;height:637px;background:linear-gradient(120deg,#8a7460 0%,#5e554f 35%,#3f3a38 60%,#6d6258 100%)}
.hero-photo{position:absolute;inset:0;background:radial-gradient(ellipse at 30% 70%,rgba(230,215,195,.35),transparent 55%),radial-gradient(ellipse at 80% 20%,rgba(255,240,220,.25),transparent 50%)}
.hero-shade{position:absolute;inset:0;background:rgba(20,20,25,.25)}
.brand{position:absolute;left:153px;top:52px;display:flex;align-items:center;gap:12px;color:var(--white);font-weight:700;font-size:34px}
.brand-dot{width:34px;height:34px;border-radius:50%;background:var(--white)}
.nav{position:absolute;left:540px;top:64px;display:flex;gap:32px;font-size:16px;font-weight:700;color:var(--white)}
.nav .active{color:var(--teal)}
.hero-title{position:absolute;left:0;width:1200px;top:270px;text-align:center;color:var(--white);font-size:40px;font-weight:700;line-height:50px}
.btn-outline{position:absolute;left:516px;top:391px;width:180px;height:46px;border:2px solid var(--white);color:var(--white);font-size:16px;font-weight:700;display:flex;align-items:center;justify-content:center;letter-spacing:.5px}
.dots{position:absolute;top:596px;left:558px;display:flex;gap:8px}
.dots span{width:13px;height:13px;border-radius:50%;background:var(--white)}
.dots span.off{background:transparent;border:2px solid var(--white)}

/* Intro */
.section-title{position:absolute;left:0;width:1200px;text-align:center;font-size:30px;font-weight:400;color:var(--text)}
.intro-sub{position:absolute;left:220px;width:760px;top:748px;text-align:center;font-size:18px;line-height:30px;color:var(--muted);font-family:"Open Sans",sans-serif}
.feature{position:absolute;width:340px}
.feature svg{position:absolute;left:0;top:0}
.feature h3{position:absolute;left:140px;top:0;width:240px;font-size:21px;line-height:25px;font-weight:400;color:var(--teal)}
.feature p{position:absolute;left:140px;top:62px;width:260px;font-family:"Open Sans",sans-serif;font-size:12px;line-height:18px;color:var(--muted)}

/* Process */
.process{position:absolute;left:0;top:1320px;width:1200px;height:507px;background:var(--grey-band)}
.step{position:absolute;width:240px}
.step h4{font-size:21px;font-weight:400}
.step p{margin-top:8px;font-family:"Open Sans",sans-serif;font-size:12px;line-height:18px;color:var(--muted)}
.step.left{text-align:right}
.step-badge{position:absolute;width:76px;height:76px;border-radius:50%;display:flex;align-items:center;justify-content:center}

/* Clients */
.client-mark{position:absolute;background:#d5d7da;border-radius:4px}

/* Testimonials */
.testimonials{position:absolute;left:0;top:2239px;width:1200px;height:406px;background:linear-gradient(100deg,var(--red) 0%,#d04a35 45%,var(--orange) 100%)}
.quote-box{position:absolute;left:309px;top:127px;width:582px;height:161px;border:2px solid rgba(255,255,255,.85)}
.quote-text{position:absolute;left:0;width:100%;top:40px;text-align:center;color:var(--white);font-size:21px;line-height:38px}
.quote-mark{position:absolute;left:565px;top:100px;width:70px;height:70px;border-radius:50%;background:var(--orange);color:var(--white);font-size:56px;font-weight:700;display:flex;align-items:center;justify-content:center;line-height:1;padding-top:18px}
.avatar{position:absolute;left:568px;top:255px;width:64px;height:64px;border-radius:50%;background:linear-gradient(#c9b8a8,#8f7b6c);border:3px solid var(--white)}
.quote-name{position:absolute;left:0;width:1200px;top:328px;text-align:center;color:var(--white);font-weight:700;font-size:17px}
.quote-role{position:absolute;left:0;width:1200px;top:352px;text-align:center;color:var(--white);font-size:13px}

/* Contact */
.contact{position:absolute;left:0;top:2645px;width:1200px;height:509px;background:linear-gradient(90deg,#e6e8ea 0%,#f4f5f6 30%,#f6f6f7 70%,#eceeef 100%)}
.field{position:absolute;width:356px;height:40px;background:var(--white);border:1px solid #d7dadd;border-radius:3px;font-family:"Open Sans",sans-serif;font-size:13px;color:#777;padding:11px 16px}
.btn-submit{position:absolute;left:519px;top:414px;width:176px;height:42px;background:var(--navy-btn);color:var(--white);font-weight:700;font-size:16px;display:flex;align-items:center;justify-content:center;border-radius:2px}

/* Footer */
.footer{position:absolute;left:0;top:3154px;width:1200px;height:316px;background:var(--teal);color:var(--white)}
.footer-col{position:absolute;top:48px}
.footer-col h5{font-size:19px;font-weight:600;margin-bottom:14px}
.footer-col li{list-style:none;font-family:"Open Sans",sans-serif;font-size:14px;line-height:28px}
.contact-row{display:flex;gap:12px;font-family:"Open Sans",sans-serif;font-size:14px;line-height:22px;margin-bottom:10px}
.social{display:flex;gap:8px;margin-top:14px}
.social span{width:28px;height:28px;border:1.5px solid var(--white);border-radius:50%}
.bottom-bar{position:absolute;left:0;top:3470px;width:1200px;height:66px;background:var(--teal-dark);color:var(--white);font-family:"Open Sans",sans-serif;font-size:13px;display:flex;align-items:center;justify-content:center}
</style>
</head>
<body>

<header class="hero">
  <div class="hero-photo" role="img" aria-label="Photo of a person typing on a laptop at a wooden desk beside a cup of coffee"></div>
  <div class="hero-shade"></div>
  <div class="brand"><span class="brand-dot"></span>Pelran Data</div>
  <nav class="nav">
    <span class="active">Home</span><span>About Us</span><span>Blog</span><span>Software Solutions</span><span>Contact</span>
  </nav>
  <h1 class="hero-title">Our Ledgerly Add-On Solutions help<br>Ambitious Businesses</h1>
  <div class="btn-outline">LEARN MORE</div>
  <div class="dots"><span></span><span class="off"></span><span class="off"></span><span class="off"></span></div>
</header>

<section>
  <h2 class="section-title" style="top:694px">Do you REALLY trust your Inventory System?</h2>
  <p class="intro-sub">Mauris neque metus malesuada nec ultricies sit amet porttitor mattis enim In massa libero interdum nec interdum vel blandit sed nulla In</p>

  <div class="feature" style="left:165px;top:896px">
    <svg width="110" height="120" viewBox="0 0 110 120" fill="none" stroke="var(--teal-icon)" stroke-width="4" stroke-linecap="round" stroke-linejoin="round">
      <rect x="8" y="8" width="94" height="68"/><line x1="2" y1="8" x2="108" y2="8"/>
      <polyline points="22,62 42,42 56,52 84,24"/><polyline points="72,24 84,24 84,36"/>
      <line x1="55" y1="76" x2="55" y2="92"/><line x1="55" y1="92" x2="40" y2="112"/><line x1="55" y1="92" x2="70" y2="112"/>
    </svg>
    <h3>Are those stock<br>levels accurate?</h3>
    <p>Mauris neque metus malesuada nec ultricies sit amet porttitor mattis enim</p>
  </div>

  <div class="feature" style="left:618px;top:890px">
    <svg width="110" height="112" viewBox="0 0 110 112" fill="none" stroke="var(--teal-icon)" stroke-width="4" stroke-linejoin="round">
      <path d="M6 36 L55 6 L104 36 V106 H6 Z"/>
      <rect x="26" y="52" width="58" height="54"/>
      <rect x="34" y="80" width="20" height="26"/><rect x="56" y="80" width="20" height="26"/><rect x="45" y="58" width="20" height="22"/>
    </svg>
    <h3>Does the Hobart<br>warehouse have stock?</h3>
    <p>Mauris neque metus malesuada nec ultricies sit amet porttitor mattis enim</p>
  </div>

  <div class="feature" style="left:162px;top:1096px">
    <svg width="130" height="110" viewBox="0 0 130 110" fill="none" stroke="var(--teal-icon)" stroke-width="4" stroke-linejoin="round" stroke-linecap="round">
      <path d="M8 86 V52 H30 L44 22 H68 V86 Z"/><line x1="44" y1="22" x2="44" y2="52"/>
      <line x1="86" y1="6" x2="86" y2="94"/><line x1="86" y1="94" x2="124" y2="94"/>
      <line x1="68" y1="70" x2="86" y2="70"/>
      <circle cx="24" cy="92" r="12"/><circle cx="60" cy="92" r="12"/>
    </svg>
    <h3 style="left:142px">How many do we<br>need to order?</h3>
    <p style="left:142px">Mauris neque metus malesuada nec ultricies sit amet porttitor mattis enim</p>
  </div>

  <div class="feature" style="left:618px;top:1096px">
    <svg width="122" height="122" viewBox="0 0 122 122" fill="none" stroke="var(--teal-icon)" stroke-width="3.5" stroke-linecap="round">
      <circle cx="61" cy="61" r="58"/>
      <path d="M61 34 C80 34 92 45 92 58 C92 71 80 82 61 82 C56 82 52 81 48 80 L36 88 L39 76 C33 71 30 65 30 58 C30 45 42 34 61 34 Z"/>
      <line x1="48" y1="52" x2="74" y2="52"/><line x1="48" y1="60" x2="74" y2="60"/><line x1="48" y1="68" x2="66" y2="68"/>
    </svg>
    <h3>Why have we sold so<br>much of that product?</h3>
    <p>Mauris neque metus malesuada nec ultricies sit amet porttitor mattis enim</p>
  </div>
</section>

<section class="process">
  <h2 class="section-title" style="top:44px">Our Process</h2>
  <svg class="abs" style="left:0;top:0" width="1200" height="507" viewBox="0 0 1200 507" fill="none">
    <circle cx="602" cy="272" r="138" stroke="#e2e2e2" stroke-width="4"/>
  </svg>
  <div class="abs" role="img" aria-label="Central decorative graphic in red, teal, orange and blue" style="left:492px;top:162px;width:220px;height:220px;border-radius:50%;background:conic-gradient(var(--step-teal) 0 25%,var(--blue) 25% 50%,var(--orange) 50% 75%,var(--red) 75% 100%);opacity:.9"></div>

  <div class="step left" style="left:168px;top:120px"><h4 style="color:var(--red)">1. Scoping</h4><p>Mauris neque metus malesuada nec ultricies sit amet porttitor mattis enim in massa libero interdum nec</p></div>
  <div class="step" style="left:799px;top:120px"><h4 style="color:var(--step-teal)">2. Implementation</h4><p>Mauris neque metus malesuada nec ultricies sit amet porttitor mattis enim in massa libero interdum nec</p></div>
  <div class="step" style="left:799px;top:330px"><h4 style="color:var(--blue)">3. Training</h4><p>Mauris neque metus malesuada nec ultricies sit amet porttitor mattis enim in massa libero interdum nec</p></div>
  <div class="step left" style="left:168px;top:330px"><h4 style="color:var(--orange)">4. Support</h4><p>Mauris neque metus malesuada nec ultricies sit amet porttitor mattis enim in massa libero interdum nec</p></div>

  <div class="step-badge" style="left:426px;top:122px;background:var(--red)">
    <svg width="40" height="40" viewBox="0 0 40 40" fill="none" stroke="#fff" stroke-width="3"><circle cx="20" cy="20" r="12"/><line x1="20" y1="2" x2="20" y2="38"/><line x1="2" y1="20" x2="38" y2="20"/></svg>
  </div>
  <div class="step-badge" style="left:707px;top:122px;background:var(--step-teal)">
    <svg width="36" height="40" viewBox="0 0 36 40" fill="none" stroke="#fff" stroke-width="3"><path d="M18 3 C27 3 32 10 32 16 C32 22 26 25 25 30 H11 C10 25 4 22 4 16 C4 10 9 3 18 3 Z"/><line x1="12" y1="35" x2="24" y2="35"/></svg>
  </div>
  <div class="step-badge" style="left:707px;top:339px;background:var(--blue)">
    <svg width="40" height="40" viewBox="0 0 40 40" fill="none" stroke="#fff" stroke-width="3"><circle cx="20" cy="20" r="7"/><circle cx="20" cy="20" r="15" stroke-dasharray="6 4"/></svg>
  </div>
  <div class="step-badge" style="left:426px;top:339px;background:var(--orange)">
    <svg width="40" height="40" viewBox="0 0 40 40" fill="none" stroke="#fff" stroke-width="3"><path d="M20 6 C30 6 36 12 36 19 C36 26 30 32 20 32 L10 36 L12 29 C7 26 4 23 4 19 C4 12 10 6 20 6 Z"/></svg>
  </div>
</section>

<section>
  <h2 class="section-title" style="top:1880px;color:#6a7076">Working with leading lights</h2>
  <div class="client-mark" style="left:270px;top:1952px;width:80px;height:60px"></div>
  <div class="client-mark" style="left:374px;top:1972px;width:112px;height:20px"></div>
  <div class="client-mark" style="left:500px;top:1970px;width:96px;height:24px"></div>
  <div class="client-mark" style="left:618px;top:1974px;width:96px;height:16px"></div>
  <div class="client-mark" style="left:728px;top:1966px;width:112px;height:32px"></div>
  <div class="client-mark" style="left:860px;top:1966px;width:102px;height:30px"></div>

  <div class="client-mark" style="left:252px;top:2046px;width:118px;height:32px"></div>
  <div class="client-mark" style="left:388px;top:2046px;width:108px;height:32px"></div>
  <div class="client-mark" style="left:512px;top:2042px;width:90px;height:40px"></div>
  <div class="client-mark" style="left:620px;top:2050px;width:110px;height:26px"></div>
  <div class="client-mark" style="left:742px;top:2048px;width:112px;height:30px"></div>
  <div class="client-mark" style="left:870px;top:2040px;width:60px;height:46px"></div>

  <div class="client-mark" style="left:247px;top:2116px;width:124px;height:38px"></div>
  <div class="client-mark" style="left:400px;top:2114px;width:100px;height:42px"></div>
  <div class="client-mark" style="left:542px;top:2114px;width:44px;height:44px;border-radius:50%"></div>
  <div class="client-mark" style="left:634px;top:2122px;width:112px;height:28px"></div>
  <div class="client-mark" style="left:780px;top:2112px;width:44px;height:46px"></div>
  <div class="client-mark" style="left:862px;top:2126px;width:116px;height:18px"></div>
</section>

<section class="testimonials">
  <h2 class="section-title" style="top:44px;color:var(--white)">Client Testimonials</h2>
  <svg class="abs" style="left:238px;top:186px" width="28" height="44" viewBox="0 0 28 44" fill="none" stroke="#fff" stroke-width="3"><polyline points="24,4 6,22 24,40"/></svg>
  <svg class="abs" style="left:932px;top:186px" width="28" height="44" viewBox="0 0 28 44" fill="none" stroke="#fff" stroke-width="3"><polyline points="4,4 22,22 4,40"/></svg>
  <div class="quote-box"><p class="quote-text">Fantastic service and a focus on ensuring value<br>is delivered in a timely manner</p></div>
  <div class="quote-mark">&ldquo;</div>
  <div class="avatar" role="img" aria-label="Client portrait photo"></div>
  <p class="quote-name">Marcus Ellery</p>
  <p class="quote-role">Director, Brightwell Partners</p>
</section>

<section class="contact" role="img" aria-label="Background photo of a white desk with keyboard, binder clips, notebook and a green cup">
  <h2 class="section-title" style="top:62px;color:var(--blue)">Get In Touch</h2>
  <div class="field" style="left:243px;top:132px">Name</div>
  <div class="field" style="left:617px;top:132px">Email address</div>
  <div class="field" style="left:243px;top:183px">Phone Number</div>
  <div class="field" style="left:617px;top:183px">Web Address</div>
  <div class="field" style="left:243px;top:234px">Company Name</div>
  <div class="field" style="left:617px;top:234px">Number of Offices</div>
  <div class="field" style="left:243px;top:292px;width:730px;height:100px">Your Enquiry</div>
  <div class="btn-submit">SUBMIT NOW</div>
</section>

<footer class="footer">
  <div class="footer-col" style="left:153px"><h5>Information</h5><ul><li>Home</li><li>Software</li><li>Solution</li><li>Our Clients</li></ul></div>
  <div class="footer-col" style="left:361px"><h5>Our Services</h5><ul><li>About Us</li><li>Our Process</li><li>How it Works</li></ul></div>
  <div class="footer-col" style="left:559px"><h5>Resources</h5><ul><li>Testimonials</li><li>Blogs</li><li>News</li><li>Contact</li></ul></div>
  <div class="footer-col" style="left:761px">
    <h5>Contact Us</h5>
    <div class="contact-row">
      <svg width="14" height="20" viewBox="0 0 14 20" fill="#fff"><path d="M7 0 C11 0 14 3 14 7 C14 12 7 20 7 20 C7 20 0 12 0 7 C0 3 3 0 7 0 Z M7 4 A3 3 0 1 0 7 10 A3 3 0 1 0 7 4 Z"/></svg>
      <span>Australia: Level 4, 88 Harbour Rd,<br>Eastvale, VIC, 3999</span>
    </div>
    <div class="contact-row">
      <svg width="16" height="16" viewBox="0 0 16 16" fill="#fff"><path d="M3 0 L6 4 L4 6 C5 8 8 11 10 12 L12 10 L16 13 L14 16 C7 16 0 9 0 2 Z"/></svg>
      <span>+61 (03) 9555 0142</span>
    </div>
    <div class="contact-row">
      <svg width="16" height="14" viewBox="0 0 16 14" fill="#fff"><path d="M0 1 H16 V13 H0 Z M1 2 L8 8 L15 2" stroke="var(--teal)" stroke-width="1.2"/></svg>
      <span>enquiries@pelrandata.example</span>
    </div>
    <div class="social"><span></span><span></span><span></span><span></span></div>
  </div>
</footer>
<div class="bottom-bar">© 2017 Company Name &nbsp;All right reserved &nbsp;Term of Use</div>

</body>
</html>
```